Trade Show booth design

I need the following designs for my trade booth:
1. backboard design 3m Wx2mH
2. Tressle table, tablecloth front panel design 1800W x 740mmH
3. Pop-up banner. I have included our logos and some design content ideas:
Headline:
"Cleaner Classrooms. Safer Schools."
Subheadline:
"Specialist Cleaning Solutions for Education Facilities"
Key Points to Grab Attention:
Healthy Environments: Create hygienic, safe learning spaces for students and staff with our expert cleaning services.
Tailored to Your Needs: Custom cleaning plans for classrooms, labs, libraries, and sports facilities.
Affordable Excellence: Premium results without premium costs – tailored plans mean you only pay for what you need.
Safety First: All staff are trained, highly vetted, and hold current Working with Children Checks (WWCC).
Eco-Conscious Cleaning: Using non-toxic, eco-friendly products certified for health and safety.
What Schools Really Need:
Reliability: Consistent, high-quality cleaning from a trusted provider.
Cost-Effectiveness: Solutions that fit tight budgets while maintaining high standards.
Expertise: Over 30 years of experience in education facility cleaning.
Disinfection Services: Focus on high-touch areas to reduce the spread of germs and ensure peace of mind.
Visual Elements:
Images of bright, clean classrooms, a happy teacher welcoming students, or students collaborating in a spotless library.
Icons representing safety (shield), hygiene (sparkling star), and eco-friendliness (leaf).
Your logo with the tagline: "Trusted by Queensland Schools Since 1995."
Call-to-Action:
"Visit us to discuss your school’s cleaning needs and book a FREE consultation."
Include contact details: Phone: 1300 649 315 | Website: www.duravoss.com.au
Target Market(s)
Education sector
Industry/Entity Type
Commercial Cleaning
Font styles to use
Other font styles liked:
- Montserrat
Look and feel

```html
<!DOCTYPE html>
<html lang="en">
<head>
<meta charset="utf-8">
<title>Duravoss – School Cleaning Backboard</title>
<link rel="stylesheet" href="https://fonts.googleapis.com/css2?family=Bebas+Neue&family=Montserrat:wght@700;800;900&family=Poppins:wght@500;700&display=swap">
<style>
  :root {
    --navy: #1d3a63;
    --navy-deep: #183255;
    --cyan: #1ab4e3;
    --cyan-bright: #22c4f0;
    --ring-light: #e4f6fc;
    --white: #ffffff;
    --ink: #1f3556;
    --stage: #f4f4f7;
  }
  * { margin: 0; padding: 0; box-sizing: border-box; }
  html, body { width: 1150px; height: 1200px; overflow: hidden; background: var(--stage); }
  .backboard {
    position: absolute; left: 20px; top: 185px; width: 1110px; height: 830px;
    background: var(--white); overflow: hidden;
    font-family: "Poppins", sans-serif; color: var(--ink);
  }
  .abs { position: absolute; }

  /* brand */
  .brand { left: 64px; top: 92px; display: flex; align-items: center; gap: 16px; }
  .brand-dot { width: 22px; height: 22px; border-radius: 50%; background: var(--navy); }
  .brand-name { font-family: "Montserrat", sans-serif; font-weight: 800; font-size: 66px; color: var(--navy); letter-spacing: -1px; line-height: 1; }

  .sparkle { fill: var(--cyan); }

  .headline-top {
    left: 64px; top: 216px; z-index: 2; white-space: nowrap;
    font-family: "Bebas Neue", sans-serif; font-size: 74px; line-height: 1;
    color: var(--cyan); letter-spacing: -0.5px;
    transform: scaleX(0.89); transform-origin: left top;
  }
  .headline-bottom { left: 62px; top: 290px; z-index: 2; white-space: nowrap; font-family: "Montserrat", sans-serif; font-weight: 800; font-size: 53px; line-height: 1; color: var(--navy); letter-spacing: -1.5px; }

  /* right visual */
  .cyan-panel { left: 720px; top: 470px; width: 390px; height: 360px; background: linear-gradient(180deg, var(--cyan-bright), var(--cyan)); }
  .ring-light { left: 542px; top: -72px; width: 610px; height: 610px; border-radius: 50%; background: var(--ring-light); }
  .sub-band { left: 59px; top: 375px; width: 800px; height: 148px; background: var(--navy); border-radius: 22px 0 0 22px; }
  .ring-navy { left: 557px; top: -57px; width: 580px; height: 580px; border-radius: 50%; background: var(--navy); }
  .photo {
    left: 610px; top: -5px; width: 476px; height: 476px; border-radius: 50%;
    border: 4px solid var(--white);
    background:
      radial-gradient(circle at 30% 25%, #fff6cf 0%, rgba(255,240,190,0) 45%),
      linear-gradient(180deg, #f3dca0 0%, #e9c27a 40%, #d99a4c 75%, #c98a45 100%);
  }

  .sub-top { left: 84px; top: 396px; white-space: nowrap; font-family: "Bebas Neue", sans-serif; font-size: 50px; line-height: 1; color: var(--white); letter-spacing: -0.3px; }
  .sub-rule { left: 84px; top: 452px; width: 474px; height: 1px; background: rgba(255,255,255,0.55); }
  .sub-bottom { left: 84px; top: 462px; white-space: nowrap; font-family: "Montserrat", sans-serif; font-weight: 800; font-size: 31px; line-height: 1; color: var(--white); letter-spacing: -0.3px; }

  /* benefits */
  .benefits { left: 74px; top: 572px; list-style: none; }
  .benefit { display: flex; align-items: flex-start; gap: 14px; font-size: 20.5px; line-height: 1.15; font-weight: 500; color: var(--ink); margin-bottom: 16px; }
  .benefit svg { flex: 0 0 24px; width: 24px; height: 24px; margin-top: 1px; }
  .benefit .label { padding-top: 1px; }

  .needs-title { left: 396px; top: 568px; font-family: "Poppins", sans-serif; font-weight: 700; font-size: 27px; line-height: 1.08; color: var(--cyan); letter-spacing: -0.3px; }
  .needs { left: 400px; top: 645px; list-style: none; }
  .need { display: flex; align-items: center; gap: 10px; font-size: 20.5px; font-weight: 500; color: var(--ink); height: 26px; margin-bottom: 14.5px; }
  .need-marker { width: 24px; height: 8px; }

  /* call to action */
  .cta-free { left: 722px; top: 528px; width: 388px; text-align: center; font-family: "Montserrat", sans-serif; font-weight: 900; font-size: 128px; line-height: 1; color: var(--white); letter-spacing: -3px; }
  .cta-consult { left: 722px; top: 651px; width: 388px; text-align: center; font-family: "Montserrat", sans-serif; font-weight: 800; font-size: 35px; line-height: 1; color: var(--white); letter-spacing: 0; }
  .phone-pill { left: 755px; top: 703px; width: 306px; height: 60px; background: var(--white); border-radius: 30px; display: flex; align-items: center; padding-left: 8px; gap: 9px; }
  .phone-icon { width: 44px; height: 44px; }
  .phone-number { font-family: "Montserrat", sans-serif; font-weight: 800; font-size: 33px; color: var(--navy); letter-spacing: -0.5px; }
  .web { left: 722px; top: 780px; width: 388px; text-align: center; font-family: "Poppins", sans-serif; font-weight: 700; font-size: 23px; color: var(--white); }
</style>
</head>
<body>
<main class="backboard">

  <div class="abs cyan-panel"></div>
  <div class="abs ring-light"></div>
  <div class="abs sub-band"></div>
  <div class="abs ring-navy"></div>
  <div class="abs photo" role="img" aria-label="Photo of a bright, sunlit empty classroom with wooden desks and chairs"></div>

  <div class="abs brand">
    <span class="brand-dot"></span>
    <span class="brand-name">Duravoss</span>
  </div>

  <svg class="abs" style="left:476px;top:168px" width="50" height="50" viewBox="0 0 50 50" aria-hidden="true">
    <path class="sparkle" d="M34 2 L36 10 L44 12 L36 14 L34 22 L32 14 L24 12 L32 10 Z"/>
    <path class="sparkle" d="M12 22 L14.5 32.5 L25 35 L14.5 37.5 L12 48 L9.5 37.5 L-1 35 L9.5 32.5 Z"/>
  </svg>

  <h1 class="abs headline-top">CLEANER CLASSROOMS</h1>
  <h2 class="abs headline-bottom">SAFER SCHOOLS</h2>

  <p class="abs sub-top">SPECIALIST CLEANING SOLUTIONS</p>
  <div class="abs sub-rule"></div>
  <p class="abs sub-bottom">FOR EDUCATION FACILITIES</p>

  <ul class="abs benefits">
    <li class="benefit">
      <svg viewBox="0 0 24 24" aria-hidden="true"><path d="M12 2 L23 11 L20 11 L20 22 L4 22 L4 11 L1 11 Z" fill="var(--cyan)"/><path d="M9 22 V15 H15 V22" fill="var(--white)"/></svg>
      <span class="label">Healthy Environments</span>
    </li>
    <li class="benefit">
      <svg viewBox="0 0 24 24" aria-hidden="true"><path d="M12 1 V10 M8 7 L12 11 L16 7" stroke="var(--navy)" stroke-width="2.6" fill="none"/><path d="M1 15 H6 V23 H1 Z" fill="var(--cyan)"/><path d="M6 16 C10 14 13 15 15 17 H19 C21 17 22 19 20 20 L14 22 H6 Z" fill="var(--cyan)"/></svg>
      <span class="label">Tailored to Your Needs</span>
    </li>
    <li class="benefit" style="margin-bottom:18px">
      <svg viewBox="0 0 24 24" aria-hidden="true"><circle cx="12" cy="12" r="10.5" fill="none" stroke="var(--cyan)" stroke-width="2.4" stroke-dasharray="3 1.5"/><circle cx="12" cy="12" r="6.5" fill="none" stroke="var(--cyan)" stroke-width="2"/><path d="M8.8 12 L11 14.3 L15.4 9.8" stroke="var(--cyan)" stroke-width="2" fill="none"/></svg>
      <span class="label">Affordable Excellence to<br>Your Needs</span>
    </li>
    <li class="benefit">
      <svg viewBox="0 0 24 24" aria-hidden="true"><path d="M12 1 L21 4.5 V11 C21 17 16.5 21 12 23 C7.5 21 3 17 3 11 V4.5 Z" fill="var(--cyan)"/><path d="M8.3 12 L11 14.6 L15.8 9.6" stroke="var(--white)" stroke-width="1.6" fill="none"/></svg>
      <span class="label">Safety First</span>
    </li>
    <li class="benefit">
      <svg viewBox="0 0 24 24" aria-hidden="true"><path d="M12 1 C15 6 19 10.5 19 15.5 C19 19.5 16 23 12 23 C8 23 5 19.5 5 15.5 C5 10.5 9 6 12 1 Z" fill="var(--cyan)"/><path d="M9 18 C9 14 11.5 12.5 15 12.5 C15 16 13 18 9 18 Z" fill="var(--white)"/></svg>
      <span class="label">Eco-Conscious Cleaning</span>
    </li>
  </ul>

  <h3 class="abs needs-title">What Schools<br>Really Need:</h3>

  <svg class="abs" style="left:618px;top:618px" width="70" height="95" viewBox="0 0 70 95" aria-hidden="true">
    <path class="sparkle" d="M25 2 L30 20 L48 25 L30 30 L25 48 L20 30 L2 25 L20 20 Z"/>
    <path class="sparkle" d="M54 67 L56 75 L64 77 L56 79 L54 87 L52 79 L44 77 L52 75 Z"/>
  </svg>

  <ul class="abs needs">
    <li class="need"><svg class="need-marker" viewBox="0 0 24 8" aria-hidden="true"><circle cx="4" cy="4" r="3.5" fill="var(--cyan)"/><path d="M6 4 H24" stroke="var(--navy)" stroke-width="1.6"/></svg>Reliability</li>
    <li class="need"><svg class="need-marker" viewBox="0 0 24 8" aria-hidden="true"><circle cx="4" cy="4" r="3.5" fill="var(--cyan)"/><path d="M6 4 H24" stroke="var(--navy)" stroke-width="1.6"/></svg>Cost-Effectiveness</li>
    <li class="need"><svg class="need-marker" viewBox="0 0 24 8" aria-hidden="true"><circle cx="4" cy="4" r="3.5" fill="var(--cyan)"/><path d="M6 4 H24" stroke="var(--navy)" stroke-width="1.6"/></svg>Expertise</li>
    <li class="need"><svg class="need-marker" viewBox="0 0 24 8" aria-hidden="true"><circle cx="4" cy="4" r="3.5" fill="var(--cyan)"/><path d="M6 4 H24" stroke="var(--navy)" stroke-width="1.6"/></svg>Disinfection Services</li>
  </ul>

  <p class="abs cta-free">FREE</p>
  <p class="abs cta-consult">CONSULTATION</p>
  <div class="abs phone-pill">
    <svg class="phone-icon" viewBox="0 0 44 44" aria-hidden="true">
      <circle cx="22" cy="22" r="21" fill="var(--navy)"/>
      <path d="M15 11 C13 12 12 14 12.5 17 C14 24 20 30 27 31.5 C30 32 32 31 33 29 L30 25 L26.5 26.5 C23 25 19 21 17.5 17.5 L19 14 Z" fill="var(--white)"/>
    </svg>
    <span class="phone-number">1300 649 315</span>
  </div>
  <p class="abs web">www.duravoss.com.au</p>

</main>
</body>
</html>
```